LAW FIRM - RE-DESIGN - (professional, excellence, tradition and innovation)

We are a premier law firm in New South Wales, Australia. We pride ourselves on being cutting edge and up to date in our market.

Our firm formed in 1874 and has a particularly strong tradition within it's geographic footprint. acting for clients over multiple generations. Despite our regional background, our reputation for excellence has enable us to remain highly visible in a large area.

We have invested heavily in ensuring future planning of this business, and do so on a recurring basis. This has lead to a review of our existing web site.

Although serviceable we feel our previous website is out-of-date and not as in touch with the modern market. We are aware that for the emerging clients a web site is often the face of a firm and a failure to hold attention on the first page may fail to capture the client.

We are seeking designs to communicate the core values of professionalism and excellence. At the same time as maintaining traditional country values of honesty, integrity and hard work we strive to embrace changes to the law and technology.

Target Market(s)

Clients of Law Firm

Industry/Entity Type

Law Firm

Coding

Coded - Design and coding required

Number of Pages Required

5+ page

Requirements
Must have
• A strong sense of professionalism and excellence with a careful balance between traditional values and innovation.
Nice to have
• We have included within our design brief links to top competitors sites to assist for design concepts.

```html
<!DOCTYPE html>
<html lang="en">
<head>
<meta charset="utf-8">
<title>KRS Law</title>
<link rel="stylesheet" href="https://fonts.googleapis.com/css2?family=Cinzel:wght@400;700&family=Oswald:wght@500&family=Open+Sans:ital,wght@0,400;0,600;0,700;1,400&display=swap">
<style>
:root{
  --blue:#1650a0;
  --blue-deep:#0f418a;
  --blue-dark:#0c3876;
  --blue-field:#2a62b0;
  --ink:#333;
  --muted:#555;
  --grey-band:#c9ced6;
  --white:#fff;
}
*{box-sizing:border-box;margin:0;padding:0}
html,body{width:1200px;height:4063px;overflow:hidden}
body{font-family:"Open Sans",Arial,sans-serif;color:var(--ink);background:var(--white);position:relative}
section,header,footer{position:absolute;left:0;width:1200px}
.serif{font-family:"Cinzel",Georgia,serif}
.wordmark{font-family:"Cinzel",Georgia,serif;font-weight:700;color:var(--blue);letter-spacing:2px}

/* header */
.site-header{top:0;height:114px;background:var(--white)}
.site-header .wordmark{position:absolute;left:76px;top:30px;font-size:44px}
.main-nav{position:absolute;right:70px;top:0;display:flex;height:114px;align-items:center;gap:0}
.main-nav a{font-size:17px;color:#333;text-decoration:none;padding:0 15px;text-transform:uppercase}
.main-nav a.active{background:var(--blue);color:#fff;height:114px;display:flex;align-items:center;padding:0 26px;position:relative}
.main-nav a.active::after{content:"";position:absolute;left:0;bottom:-14px;border-left:41px solid transparent;border-right:41px solid transparent;border-top:14px solid var(--blue)}

/* hero */
.hero{top:114px;height:563px;background:linear-gradient(180deg,#7f98b4 0%,#5d7895 40%,#2c3d55 75%,#1c2534 100%)}
.hero h1{position:absolute;top:150px;width:100%;text-align:center;font-family:"Oswald",Arial,sans-serif;font-weight:500;font-size:86px;color:#fff;letter-spacing:3px}
.hero p{position:absolute;top:254px;left:200px;width:800px;text-align:center;font-style:italic;font-size:24px;line-height:36px;color:#fff}
.hero .actions{position:absolute;top:343px;width:100%;display:flex;justify-content:center;gap:14px}
.btn{display:inline-block;font-family:"Cinzel",Georgia,serif;font-weight:700;font-size:20px;color:#fff;text-decoration:none;padding:0 22px;height:56px;line-height:54px;letter-spacing:1px}
.btn-ghost{border:2px solid #fff}
.btn-solid{background:var(--blue)}

/* welcome */
.welcome{top:677px;height:249px;background:var(--blue);color:#fff;text-align:center}
.welcome h2{margin-top:50px;font-size:48px;font-weight:400}
.welcome p{margin:14px auto 0;width:990px;font-size:15px;line-height:26px}
.welcome svg{position:absolute;left:588px;top:202px}

/* about */
.about{top:926px;height:437px}
.about h2{position:absolute;left:76px;top:52px;font-size:50px;color:var(--blue);font-weight:400}
.about .copy{position:absolute;left:76px;top:116px;width:630px;font-size:15px;line-height:26px;color:var(--muted)}
.about .copy p+p{margin-top:12px}
.about .btn{position:absolute;left:76px;top:318px;background:var(--blue);height:56px}
.about .team-photo{position:absolute;left:745px;top:65px;width:374px;height:304px;border:8px solid #e6e6e6;background:linear-gradient(135deg,#8c98a6,#55606e 55%,#2f3742)}

/* services */
.services{top:1363px;height:444px;background:linear-gradient(180deg,#d4d8de,#b7bec8)}
.services h2{position:absolute;top:56px;width:100%;text-align:center;font-size:48px;color:var(--blue);font-weight:400}
.service-card{position:absolute;top:140px;width:249px;height:239px;background:var(--blue)}
.service-card .ph{height:168px}
.service-card h3{height:71px;display:flex;align-items:center;justify-content:center;text-align:center;font-family:"Cinzel",Georgia,serif;font-weight:700;font-size:18px;line-height:22px;color:#fff}
.slider-arrow{position:absolute}

/* testimonial */
.testimonial{top:1807px;height:190px;background:var(--blue);color:#fff}
.testimonial .quote-badge{position:absolute;left:80px;top:46px}
.testimonial blockquote{position:absolute;left:236px;top:46px;width:890px;font-size:15px;line-height:28px;font-style:italic}
.testimonial cite{position:absolute;right:76px;top:135px;font-style:normal;font-family:"Cinzel",Georgia,serif;font-weight:700;font-size:16px}

/* philosophy */
.philosophy{top:1997px;height:292px}
.philosophy h2{position:absolute;left:76px;top:54px;font-size:48px;color:var(--blue);font-weight:400}
.philosophy .copy{position:absolute;left:76px;top:126px;width:700px;font-size:15px;line-height:26px;color:var(--muted)}
.philosophy .copy p+p{margin-top:12px}
.philosophy .wordmark{position:absolute;left:880px;top:90px;font-size:78px}

/* partners */
.partners{top:2289px;height:591px;background:linear-gradient(180deg,#e2e4e8,#b9bfc8)}
.partners h2{position:absolute;top:56px;width:100%;text-align:center;font-size:48px;color:var(--blue);font-weight:400}
.partners .intro{position:absolute;top:114px;left:200px;width:800px;text-align:center;font-size:15px;line-height:26px;color:var(--muted)}
.partner-card{position:absolute;top:203px;width:290px;height:320px;background:#fff;text-align:center}
.partner-card.featured{border-bottom:5px solid var(--blue)}
.partner-card .portrait{width:120px;height:120px;border-radius:50%;margin:33px auto 0;background:radial-gradient(circle at 50% 40%,#9a8070,#4a3a33);border:4px solid #e5e5e5}
.partner-card h3{margin-top:28px;font-family:"Cinzel",Georgia,serif;font-weight:700;font-size:21px;color:var(--blue)}
.partner-card p{margin:10px auto 0;width:230px;font-size:14px;line-height:24px;color:var(--muted)}

/* contact */
.contact{top:2880px;height:471px;background:var(--blue);color:#fff;text-align:center}
.contact h2{margin-top:56px;font-size:48px;font-weight:400}
.contact .intro{margin:10px auto 0;width:560px;font-size:15px;line-height:26px}
.field{position:absolute;background:var(--blue-field);color:#dbe6f6;font-size:14px;text-align:left;padding:10px 12px;border:1px solid #3a72c0}
.field svg{position:absolute;right:12px;top:18px}
.contact .submit{position:absolute;left:523px;top:357px;width:154px;height:54px;border:2px solid #fff;font-family:"Cinzel",Georgia,serif;font-weight:700;font-size:20px;line-height:50px;letter-spacing:1px}

/* news */
.news{top:3351px;height:415px}
.news h2{position:absolute;top:52px;width:100%;text-align:center;font-size:48px;color:var(--blue);font-weight:400}
.news-card{position:absolute;top:133px;width:503px;height:216px;background:#eee}
.news-card .ph{position:absolute;left:0;top:0;width:268px;height:216px}
.news-card .date{position:absolute;left:206px;top:24px;width:62px;height:72px;background:var(--blue);color:#fff;text-align:center;font-size:26px;font-weight:700;line-height:34px;padding-top:6px}
.news-card .date span{display:block;font-size:14px;font-weight:400;line-height:20px}
.news-card h3{position:absolute;left:282px;top:24px;font-family:"Cinzel",Georgia,serif;font-weight:700;font-size:21px;color:var(--blue)}
.news-card p{position:absolute;left:282px;top:62px;width:200px;font-size:14px;line-height:24px;color:var(--muted)}

/* footer */
.site-footer{top:3766px;height:238px;background:var(--blue);color:#fff}
.office{position:absolute;top:38px;width:250px}
.office h4{font-family:"Cinzel",Georgia,serif;font-weight:700;font-size:18px;margin-bottom:18px}
.office .row{display:flex;gap:14px;font-size:14px;line-height:20px;margin-bottom:12px}
.office .row svg{flex:none;margin-top:2px}
.site-footer .wordmark{position:absolute;left:905px;top:80px;color:#fff;font-size:68px}
.bottom-bar{top:4004px;height:59px;background:var(--blue-dark);color:#fff;font-size:14px}
.bottom-bar .copy{position:absolute;left:76px;top:19px}
.bottom-bar nav{position:absolute;right:76px;top:19px;display:flex;gap:26px}
.bottom-bar nav a{color:#fff;text-decoration:none}
</style>
</head>
<body>

<header class="site-header">
  <div class="wordmark">KRS LAW</div>
  <nav class="main-nav">
    <a class="active" href="#">Home</a>
    <a href="#">About Us</a>
    <a href="#">Services</a>
    <a href="#">Our People</a>
    <a href="#">FAQ's</a>
    <a href="#">Contact Us</a>
  </nav>
</header>

<section class="hero" role="img" aria-label="Photo of business people in silhouette around a boardroom table before tall windows">
  <h1>KRS LAW</h1>
  <p>KRS Law is a legal firm geographically based within the New England region of New South Wales, Australia.</p>
  <div class="actions">
    <a class="btn btn-ghost" href="#">KNOW MORE</a>
    <a class="btn btn-solid" href="#">CONTACT US</a>
  </div>
</section>

<section class="welcome">
  <h2 class="serif">WELCOME TO KRS LAW</h2>
  <p>KRS Law has been in existence since 1874 originally starting out as the firm Walter Haig of Glen Innes. In 1894 Walter Haig was acquired by Colonel RT Kemp. The firm became known as HL Kemp &amp; Co. until early 1970 when it became Kemp &amp; Co, Kemp Ross &amp; Co in 1979 and Kemp Ross &amp; Sutton in 1982.</p>
  <svg width="24" height="20" viewBox="0 0 24 20" fill="none" stroke="#fff" stroke-width="2.5"><path d="M4 2l8 7 8-7M4 10l8 7 8-7"/></svg>
</section>

<section class="about">
  <h2 class="serif">ABOUT KRS LAW</h2>
  <div class="copy">
    <p>KRS Law has been in existence since 1874 originally starting out as the firm Walter Haig of Glen Innes. In 1894 Walter Haig was acquired by Colonel RT Kemp. The firm became known as HL Kemp &amp; Co. until early 1970 when it became Kemp &amp; Co, Kemp Ross &amp; Co in 1979 and Kemp Ross &amp; Sutton in 1982.</p>
    <p>In December 1999, the firm opened an office in Inverell taking over the practice of LM Grant &amp; Associates. This was followed by the incorporation of Farrow &amp; Co in December 2000 and the Armidale office moved to larger premises in Marsh Street.</p>
  </div>
  <a class="btn" href="#">KNOW MORE</a>
  <div class="team-photo" role="img" aria-label="Group photo of the firm's four lawyers in business suits"></div>
</section>

<section class="services">
  <h2 class="serif">OUR SERVICES</h2>
  <svg class="slider-arrow" style="left:26px;top:230px" width="14" height="40" viewBox="0 0 14 40" fill="none" stroke="#fff" stroke-width="2"><path d="M12 2L2 20l10 18"/></svg>
  <svg class="slider-arrow" style="right:26px;top:230px" width="14" height="40" viewBox="0 0 14 40" fill="none" stroke="#fff" stroke-width="2"><path d="M2 2l10 18L2 38"/></svg>
  <div class="service-card" style="left:76px">
    <div class="ph" role="img" aria-label="Photo of a modern building facade" style="background:linear-gradient(160deg,#c8d6e6,#5d7896)"></div>
    <h3>BUILDING &amp;<br>CONSTRUCTION</h3>
  </div>
  <div class="service-card" style="left:341px">
    <div class="ph" role="img" aria-label="Photo of a business handshake" style="background:linear-gradient(160deg,#dfe7f1,#6f87a6)"></div>
    <h3>CORPORATE &amp;<br>COMMERCIAL</h3>
  </div>
  <div class="service-card" style="left:607px">
    <div class="ph" role="img" aria-label="Photo of handcuffed hands" style="background:linear-gradient(160deg,#6e5a4c,#241c18)"></div>
    <h3>CRIMINAL LAW</h3>
  </div>
  <div class="service-card" style="left:872px">
    <div class="ph" role="img" aria-label="Photo of a hand signing a contract" style="background:linear-gradient(160deg,#f0ece6,#a89f94)"></div>
    <h3>EMPLOYMENT LAW</h3>
  </div>
</section>

<section class="testimonial">
  <svg class="quote-badge" width="130" height="100" viewBox="0 0 130 100">
    <circle cx="80" cy="50" r="46" fill="#c9b8aa" stroke="#fff" stroke-width="4" role="img" aria-label="Client portrait"/>
    <circle cx="34" cy="50" r="32" fill="#fff"/>
    <text x="34" y="72" text-anchor="middle" font-family="Georgia,serif" font-size="58" font-weight="700" fill="#1650a0">“</text>
  </svg>
  <blockquote>" Lorem Ipsum is simply dummy text of the printing and typesetting industry. Lorem Ipsum has been the industry's standard dummy text ever since the 1500s, when an unknown printer took a galley of type and scrambled it to make a type specimen book. It has survived not only five centuries, but also the leap into electronic typesetting "</blockquote>
  <cite>— CLIENT NAME</cite>
</section>

<section class="philosophy">
  <h2 class="serif">OUR PHILOSOPHY</h2>
  <div class="copy">
    <p>Driven by quality legal work and service, KRS Law is founded on and values integrity, honesty, personal excellence, mutual respect and commitment to team work.</p>
    <p>KRS Law is built on strength, independence, integrity and an enthusiasm for the law.</p>
  </div>
  <div class="wordmark">KRS LAW</div>
</section>

<section class="partners">
  <h2 class="serif">OUR PARTNERS</h2>
  <p class="intro">Lorem Ipsum is simply dummy text of the printing and typesetting industry. Lorem Ipsum has been the industry's standard dummy text ever since the 1500s, when an unknown printer took a galley.</p>
  <svg class="slider-arrow" style="left:74px;top:340px" width="14" height="40" viewBox="0 0 14 40" fill="none" stroke="#fff" stroke-width="2"><path d="M12 2L2 20l10 18"/></svg>
  <svg class="slider-arrow" style="right:74px;top:340px" width="14" height="40" viewBox="0 0 14 40" fill="none" stroke="#fff" stroke-width="2"><path d="M2 2l10 18L2 38"/></svg>
  <div class="partner-card" style="left:144px">
    <div class="portrait" role="img" aria-label="Portrait of Peter Ross"></div>
    <h3>PETER ROSS</h3>
    <p>Currently the senior partner of KRS Law, Peter Ross was admitted as a solicitor in 1977 .</p>
  </div>
  <div class="partner-card featured" style="left:455px">
    <div class="portrait" role="img" aria-label="Portrait of Malcolm Sutton"></div>
    <h3>MALCOLM SUTTON</h3>
    <p>As senior partner of KRS Law along-side Peter Ross, Mal was admitted as a solicitor in 1977.</p>
  </div>
  <div class="partner-card" style="left:769px">
    <div class="portrait" role="img" aria-label="Portrait of Anne Ross"></div>
    <h3>ANNE ROSS</h3>
    <p>Anne Ross was admitted as a solicitor in July 2006 after completing her degrees in Economics/Law.</p>
  </div>
</section>

<section class="contact">
  <h2 class="serif">CONTACT US</h2>
  <p class="intro">If you have a legal query leave your name, contact details and query, and one of our friendly staff will get in contact with you.</p>
  <div class="field" style="left:217px;top:187px;width:361px;height:44px">Name*</div>
  <div class="field" style="left:588px;top:187px;width:394px;height:44px">Phone*</div>
  <div class="field" style="left:217px;top:241px;width:361px;height:44px">Email*</div>
  <div class="field" style="left:588px;top:241px;width:394px;height:98px">Name*</div>
  <div class="field" style="left:217px;top:295px;width:361px;height:44px">Subjects*
    <svg width="12" height="8" viewBox="0 0 12 8"><path d="M0 0h12L6 8z" fill="#fff"/></svg>
  </div>
  <div class="submit">SUBMIT</div>
</section>

<section class="news">
  <h2 class="serif">LATEST NEWS</h2>
  <article class="news-card" style="left:76px">
    <div class="ph" role="img" aria-label="Photo of business people meeting by an office window" style="background:linear-gradient(160deg,#dce6f0,#7790ac)"></div>
    <div class="date">08<span>Feb</span></div>
    <h3>NEWS TITLE</h3>
    <p>Lorem Ipsum is simply dummy text of the printing &amp; type is setting industry Ipsum has the industry's standard dummy text ever since the.</p>
  </article>
  <article class="news-card" style="left:620px">
    <div class="ph" role="img" aria-label="Photo of a hand writing with a pen on documents" style="background:linear-gradient(160deg,#f1e6d6,#b79c7c)"></div>
    <div class="date">08<span>Feb</span></div>
    <h3>NEWS TITLE</h3>
    <p>Lorem Ipsum is simply dummy text of the printing &amp; type is setting industry Ipsum has the industry's standard dummy text ever since the.</p>
  </article>
</section>

<footer class="site-footer">
  <div class="office" style="left:76px">
    <h4>ARMIDALE OFFICE</h4>
    <div class="row"><svg width="16" height="20" viewBox="0 0 16 20" fill="none" stroke="#fff" stroke-width="1.6"><path d="M8 19s7-7 7-11A7 7 0 0 0 1 8c0 4 7 11 7 11z"/><circle cx="8" cy="8" r="2.5"/></svg><span>Suite 9 Elm Arcade 42-44 Kent Street Armidale</span></div>
    <div class="row"><svg width="16" height="16" viewBox="0 0 16 16" fill="none" stroke="#fff" stroke-width="1.6"><path d="M3 1h3l1.5 4-2 1.5a9 9 0 0 0 4 4L11 8.5l4 1.5v3a2 2 0 0 1-2 2A12 12 0 0 1 1 3a2 2 0 0 1 2-2z"/></svg><span>02 5550 1200</span></div>
    <div class="row"><svg width="16" height="16" viewBox="0 0 16 16" fill="none" stroke="#fff" stroke-width="1.6"><rect x="2" y="6" width="12" height="8"/><path d="M4 6V1h8v5"/></svg><span>02 5550 1233</span></div>
  </div>
  <div class="office" style="left:344px">
    <h4>GLEN INNES OFFICE</h4>
    <div class="row"><svg width="16" height="20" viewBox="0 0 16 20" fill="none" stroke="#fff" stroke-width="1.6"><path d="M8 19s7-7 7-11A7 7 0 0 0 1 8c0 4 7 11 7 11z"/><circle cx="8" cy="8" r="2.5"/></svg><span>118 Park Street<br>Glen Innes</span></div>
    <div class="row"><svg width="16" height="16" viewBox="0 0 16 16" fill="none" stroke="#fff" stroke-width="1.6"><path d="M3 1h3l1.5 4-2 1.5a9 9 0 0 0 4 4L11 8.5l4 1.5v3a2 2 0 0 1-2 2A12 12 0 0 1 1 3a2 2 0 0 1 2-2z"/></svg><span>02 5550 2200</span></div>
    <div class="row"><svg width="16" height="16" viewBox="0 0 16 16" fill="none" stroke="#fff" stroke-width="1.6"><rect x="2" y="6" width="12" height="8"/><path d="M4 6V1h8v5"/></svg><span>02 5550 2244</span></div>
  </div>
  <div class="office" style="left:610px">
    <h4>GUYRA OFFICE</h4>
    <div class="row"><svg width="16" height="20" viewBox="0 0 16 20" fill="none" stroke="#fff" stroke-width="1.6"><path d="M8 19s7-7 7-11A7 7 0 0 0 1 8c0 4 7 11 7 11z"/><circle cx="8" cy="8" r="2.5"/></svg><span>27 Ridge Street<br>Guyra (By Appointment)</span></div>
    <div class="row"><svg width="16" height="16" viewBox="0 0 16 16" fill="none" stroke="#fff" stroke-width="1.6"><path d="M3 1h3l1.5 4-2 1.5a9 9 0 0 0 4 4L11 8.5l4 1.5v3a2 2 0 0 1-2 2A12 12 0 0 1 1 3a2 2 0 0 1 2-2z"/></svg><span>02 5550 1200</span></div>
    <div class="row"><svg width="16" height="16" viewBox="0 0 16 16" fill="none" stroke="#fff" stroke-width="1.6"><rect x="2" y="6" width="12" height="8"/><path d="M4 6V1h8v5"/></svg><span>02 5550 1233</span></div>
  </div>
  <div class="wordmark">KRS LAW</div>
</footer>

<footer class="bottom-bar">
  <div class="copy">©KRS Law 2017. All Rights Reserved.</div>
  <nav>
    <a href="#">Home</a><a href="#">About Us</a><a href="#">Services</a><a href="#">Our People</a><a href="#">Faq's</a><a href="#">Contact Us</a>
  </nav>
</footer>

</body>
</html>
```